Need Letterhead and Business Card

I have a logo but i need new letterhead and biz cards. We are a real estate investment firm so we need very professional but also do not want to be old fashioned. We have 3 locations; Singapore, New York and Ponte Vedra Florida. I can provide full addresses if needed. If you have adjustments to our logo you would recommend we are open to them.
I will be putting in a separate project but we also need a template for our own powerpoint slide presentations and website.

Industry/Entity Type

Real Estate

```html
<!DOCTYPE html>
<html lang="en">
<head>
<meta charset="utf-8">
<title>Halden Letterhead</title>
<link rel="stylesheet" href="https://fonts.googleapis.com/css2?family=Questrial&family=Lato:wght@400;700&display=swap">
<style>
  :root {
    --backdrop: #e4e8eb;
    --paper: #ffffff;
    --paper-back: #f4f4f4;
    --brand-blue: #0d4a80;
    --ink: #1a1a1a;
    --gold: #f0ac33;
    --rule: #1d4f86;
    --footer-mark: #9fb6cc;
    --map-tone: #eef1f4;
  }
  * { box-sizing: border-box; margin: 0; padding: 0; }
  html, body { width: 1200px; height: 924px; overflow: hidden; }
  body {
    background: var(--backdrop);
    font-family: "Questrial", "Century Gothic", sans-serif;
    color: var(--ink);
    position: relative;
  }
  .sheet {
    position: absolute;
    top: 46px;
    width: 512px;
    height: 696px;
    border-radius: 12px;
    overflow: hidden;
    box-shadow: 0 2px 6px rgba(0,0,0,0.18);
  }
  .sheet--front { left: 43px; background: var(--paper); }
  .sheet--back { left: 635px; background: var(--paper-back); }

  .brand-name {
    position: absolute;
    font-family: "Questrial", "Century Gothic", sans-serif;
    color: var(--brand-blue);
    letter-spacing: 1px;
    line-height: 1;
  }
  .sheet--front .brand-name { left: 43px; top: 50px; font-size: 40px; }
  .sheet--back .brand-name { left: 0; right: 0; top: 570px; text-align: center; font-size: 52px; }

  .contact {
    position: absolute;
    left: 333px;
    top: 54px;
    list-style: none;
    font-size: 10.5px;
  }
  .contact li { display: flex; align-items: center; height: 17.5px; }
  .contact svg { width: 10px; height: 10px; margin-right: 6px; fill: var(--brand-blue); }

  .header-rule {
    position: absolute;
    left: 37px; right: 40px; top: 120px;
    height: 2px; background: var(--rule);
  }

  .world-map {
    position: absolute;
    left: 30px; top: 250px;
    width: 450px; height: 220px;
    background: radial-gradient(ellipse at center, var(--map-tone) 0%, rgba(238,241,244,0) 70%);
  }

  .letter-body {
    position: absolute;
    left: 44px; top: 138px;
    width: 425px;
    font-size: 10.6px;
    line-height: 17.8px;
    text-align: justify;
  }
  .letter-body p { margin-bottom: 17.8px; }

  .signature {
    position: absolute;
    right: 44px; top: 577px;
    text-align: left;
  }
  .signature__name { font-size: 13px; }
  .signature__title { font-size: 9.5px; margin-top: 8px; }

  .office-band {
    position: absolute;
    left: 0; right: 0; bottom: 0;
    height: 57px;
    background: var(--brand-blue);
  }
  .offices {
    position: absolute;
    left: 37px; top: 7px;
    font-family: "Lato", sans-serif;
    font-size: 8.3px;
    border-collapse: collapse;
  }
  .offices th { color: #fff; font-weight: 700; text-align: left; padding: 0 6px 0 0; height: 15.5px; width: 80px; }
  .offices td { color: var(--gold); font-weight: 700; }
  .office-band .band-name {
    position: absolute;
    right: 36px; top: 14px;
    font-family: "Questrial", "Century Gothic", sans-serif;
    font-size: 28px;
    color: var(--footer-mark);
    letter-spacing: 1px;
  }
</style>
</head>
<body>
  <section class="sheet sheet--front">
    <div class="brand-name">HALDEN</div>

    <ul class="contact">
      <li><svg viewBox="0 0 10 10"><path d="M1 3 Q5 0 9 3 L8 4.5 L6.5 3.5 L3.5 3.5 L2 4.5 Z M2.5 5 H7.5 L8.5 9 H1.5 Z"/></svg>+65 6100 2741</li>
      <li><svg viewBox="0 0 10 10"><path d="M0.5 2 H9.5 V8 H0.5 Z M1 2.5 L5 5.5 L9 2.5" fill="var(--brand-blue)"/><path d="M1 2.6 L5 5.4 L9 2.6" stroke="#fff" stroke-width="0.8" fill="none"/></svg>info@haldenrealty.com</li>
      <li><svg viewBox="0 0 10 10"><path d="M4 6 L6 4" stroke="var(--brand-blue)" stroke-width="1.2"/><rect x="0.8" y="5" width="4.5" height="2.6" rx="1.3" transform="rotate(-45 3 6.3)" fill="none" stroke="var(--brand-blue)" stroke-width="1"/><rect x="4.6" y="1.6" width="4.5" height="2.6" rx="1.3" transform="rotate(-45 6.9 2.9)" fill="none" stroke="var(--brand-blue)" stroke-width="1"/></svg>www.haldenrealty.com</li>
    </ul>

    <div class="header-rule"></div>

    <div class="world-map" role="img" aria-label="Faint world map watermark behind the letter text"></div>

    <div class="letter-body">
      <p>Lorem ipsum dolor sit amet, consectetur adipiscing elit. Donec orci purus, luctus vitae dignissim eu, iaculis sed purus. Vivamus faucibus, ipsum nec aliquet viverra, leo mauris condimentum ligula, sit amet sagittis enim ligula quis arcu. Nam egestas tortor id nisi porttitor mattis. In tortor ante, ultricies in suscipit a, tempus non massa. Vivamus et auctor mi. Fusce vel massa nulla. Phasellus nec eros mauris, et scelerisque orci. Donec malesuada orci vitae nulla accumsan porta a id massa.</p>
      <p>Quisque accumsan iaculis magna sit amet fringilla. Maecenas consequat, magna eget tincidunt semper, odio nibh rutrum mi, id feugiat ante nisi eu risus. Vestibulum nunc orci, rhoncus a placerat in, ultricies in mi. Cras mattis varius eros, vel fringilla nisi suscipit eget. Quisque scelerisque sagittis nulla at porttitor. Mauris a justo et tellus interdum tristique. Sed id augue vitae urna euismod commodo aliquet a quam. Pellentesque arcu velit, cursus et malesuada ut, consequat et diam. Nullam erat sem, rhoncus id ullamcorper vitae, rhoncus et arcu. In ultricies ultricies nulla.</p>
      <p>Kut rutrum nisi iaculis at. Donec eu magna a metus ornare faucibus. Fusce aliquet faucibus ultricies. Morbi semper, est id tincidunt gravida, sem arcu adipiscing lacus, ac bibendum nulla leo eu purus. Quisque nec diam sed risus consectetur a ccumsan quis quis nibh. Vestibulum id purus lorem. Donec eu magna a metus ornare faucibus. Fusce aliquet faucibus ultricies. Morbi semper, est id tincidunt gravida, sem arcu adipiscing lacus, ac bibendum nulla leo eu purus. Quisque nec diam sed risus consectetur a ccumsan quis quis nibh. Vestibulum id purus lorem.</p>
    </div>

    <div class="signature">
      <div class="signature__name">Owen Hartley</div>
      <div class="signature__title">Co-Founder &amp; CEO</div>
    </div>

    <footer class="office-band">
      <table class="offices">
        <tr><th>Singapore:</th><td>42 Marina Crescent, Singapore, 018990</td></tr>
        <tr><th>New York:</th><td>780 Hudson Street, New York, NY 10014</td></tr>
        <tr><th>Ponte Vedra Florida:</th><td>315 Palm Terrace, Florida, 32082</td></tr>
      </table>
      <div class="band-name">HALDEN</div>
    </footer>
  </section>

  <section class="sheet sheet--back">
    <div class="brand-name">HALDEN</div>
  </section>
</body>
</html>
```